Sponsorship and registration document for Charity Golf Day 2022

The project requires 2 documents to be updated to look more graphically savvy and professionally presentable.
1. Charity golf day sponsorship document
2. One page registration document.
The text has been completed. Text not to be changed - just graphics.
New images would be preferred.
The logos have been provided.

Target Market(s)

Corporate Sponsors and Golf players

Requirements
Must have
• Golf Theme

```html
<!DOCTYPE html>
<html lang="en">
<head>
<meta charset="utf-8">
<title>Charity Golf Day – Sponsorship Proposal</title>
<link href="https://fonts.googleapis.com/css2?family=Montserrat:ital,wght@0,500;0,600;0,700;0,800;0,900;1,800;1,900&family=Open+Sans:wght@400;600&display=swap" rel="stylesheet">
<style>
:root{
  --backdrop:#4a4b4d;
  --paper:#ffffff;
  --navy:#1d4a8c;
  --blue:#2d5592;
  --green:#7cc242;
  --charcoal:#3d4147;
  --grey:#b7babd;
  --ink:#1a1a1a;
  --orange:#f0a12c;
  --turf-light:#9cc84a;
  --turf-mid:#5f8a2a;
  --turf-dark:#33501a;
  --heading:"Montserrat",sans-serif;
  --body:"Open Sans",sans-serif;
}
*{margin:0;padding:0;box-sizing:border-box}
html,body{width:1200px;height:606px;overflow:hidden;background:var(--backdrop)}
.spread{position:relative;width:1200px;height:606px}
.page{position:absolute;top:60px;width:343px;height:486px;background:var(--paper);overflow:hidden;box-shadow:3px 4px 8px rgba(0,0,0,.45)}
.page--cover{left:64px}
.page--contents{left:428px}
.page--letter{left:792px}
.abs{position:absolute}

/* image areas */
.cover-photo{left:0;top:0;width:343px;height:226px;background:radial-gradient(ellipse at 70% 55%,var(--turf-light) 0%,var(--turf-mid) 50%,var(--turf-dark) 100%)}
.cover-band{left:0;top:226px;width:343px;height:6px;background:linear-gradient(90deg,var(--blue),var(--green))}
.header-band{left:0;width:343px;height:22px;background:linear-gradient(90deg,var(--blue) 0%,var(--blue) 55%,var(--grey) 100%)}

/* cover */
.cover-title{left:0;width:343px;text-align:center;font-family:var(--heading);font-weight:900;color:#fff;text-shadow:2px 2px 0 #111;line-height:1}
.cover-title--small{top:29px;font-size:30px;padding-left:8px}
.cover-title--large{top:60px;font-size:43px;letter-spacing:.5px}
.cover-date{left:28px;top:243px;font-family:var(--heading);font-weight:700;font-size:14px;line-height:15px;color:var(--navy)}
.cover-rule{height:1px;background:var(--green)}
.cover-venue{left:28px;top:278px;font-family:var(--heading);font-weight:900;font-style:italic;font-size:20px;line-height:22px;color:var(--green)}
.cover-heading{left:26px;font-family:var(--heading);font-weight:900;font-size:29px;line-height:1;color:var(--navy)}
.cover-panel{left:0;top:382px;width:215px;height:68px;background:var(--navy);clip-path:polygon(0 0,100% 0,88% 100%,0 100%)}
.cover-cause{left:28px;top:389px;width:160px}
.cover-cause h2{font-family:var(--heading);font-weight:800;font-size:11px;line-height:14px;color:#fff}
.cover-cause p{margin-top:3px;font-family:var(--body);font-size:6.6px;line-height:7.2px;color:var(--green)}
.cover-web{left:0;width:343px;top:464px;text-align:center;font-family:var(--heading);font-weight:600;font-size:8px;letter-spacing:3.4px;color:var(--navy)}

/* club name */
.club{display:flex;align-items:center;gap:5px}
.club-name{font-family:var(--body);font-weight:600;color:var(--navy);line-height:1.05}
.club-mark{border-radius:50%;background:var(--orange)}

/* inner page header */
.doc-title{right:34px;text-align:right;font-family:var(--heading);font-weight:800;font-size:8.5px;line-height:10.5px;color:var(--navy)}
.doc-title em{font-style:italic}

/* contents */
.contents-heading{left:34px;top:171px;font-family:var(--heading);font-weight:900;font-size:17px;color:var(--navy)}
.contents-list{left:34px;top:206px;width:275px;list-style:none}
.contents-list li{display:flex;justify-content:space-between;font-family:var(--heading);font-weight:800;font-size:9.6px;height:18.5px;color:var(--ink)}
.contact{left:34px;font-family:var(--heading);font-weight:500;font-size:6.8px;line-height:8.3px;color:var(--ink)}
.contact h3{font-size:12px;font-weight:600;line-height:12px}

/* letter */
.letter-lead{left:23px;top:159px;width:295px;font-family:var(--heading);font-weight:800;font-size:8.4px;line-height:10.4px;color:var(--navy)}
.letter-text{left:23px;font-family:var(--body);font-size:6.9px;line-height:8.3px;color:var(--ink)}
.letter-text--narrow{width:183px;text-align:justify}
.ticks{list-style:none}
.ticks li{display:flex;align-items:center;gap:5px}
.ticks svg{width:7px;height:7px;flex:none}
.signoff{left:225px;font-family:var(--body);font-size:6.9px;line-height:8.3px;color:var(--ink)}
</style>
</head>
<body>
<main class="spread">

  <!-- Cover -->
  <section class="page page--cover">
    <div class="abs cover-photo" role="img" aria-label="Photo of a golf ball on a tee beside a driver on green turf"></div>
    <div class="abs cover-band" role="img" aria-label="Decorative colour band in blue and green"></div>

    <h1 class="abs cover-title cover-title--small">CHARITY</h1>
    <div class="abs cover-title cover-title--large">GOLF DAY</div>

    <p class="abs cover-date">Friday 25<br>March 2022</p>
    <div class="abs cover-rule" style="left:28px;top:275px;width:147px"></div>
    <p class="abs cover-venue">Elmwood Golf Club</p>
    <div class="abs cover-rule" style="left:28px;top:302px;width:171px"></div>
    <p class="abs cover-heading" style="top:309px">SPONSORSHIP</p>
    <p class="abs cover-heading" style="top:338px">PROPOSAL</p>

    <div class="abs cover-panel"></div>
    <div class="abs cover-cause">
      <h2>SUPPORTING PROSTATE CANCER RESEARCH</h2>
      <p>Help us hit prostate cancer off the green and beat the most common cancer in Australian men.</p>
    </div>

    <div class="abs club" style="left:212px;top:398px">
      <div class="club-name" style="font-size:16px">Fairway<br>Eastbrook</div>
      <div class="club-mark" style="width:38px;height:38px"></div>
    </div>

    <p class="abs cover-web">www.fce.org.au/golf-day</p>
  </section>

  <!-- Contents -->
  <section class="page page--contents">
    <div class="abs club" style="left:34px;top:17px">
      <div class="club-name" style="font-size:13px">Fairway<br>Eastbrook</div>
      <div class="club-mark" style="width:32px;height:32px"></div>
    </div>
    <p class="abs doc-title" style="top:69px">CHARITY GOLF DAY<br><em>SPONSORSHIP PROPOSAL</em></p>
    <div class="abs header-band" style="top:106px" role="img" aria-label="Decorative header band in blue, green and grey"></div>

    <h2 class="abs contents-heading">CONTENTS:</h2>
    <ol class="abs contents-list">
      <li><span>Charity Golf Day Invitation</span><span>2</span></li>
      <li><span>About Prostate Cancer</span><span>3</span></li>
      <li><span>Why are we asking you to be involved</span><span>3</span></li>
      <li><span>What to expect</span><span>4</span></li>
      <li><span>Sponsorship Opportunities</span><span>5</span></li>
      <li><span>Application Form</span><span>7</span></li>
    </ol>

    <div class="abs contact" style="top:350px">
      <h3>Contact :</h3>
      <p>Maria (Kostas) Bellamy<br>Convenor<br>Co - President, Fairway Club of Eastbrook<br>Mobile: 0400 555 123<br>Email: maria.bellamy@example.com<br>Web: www.fce.org.au/golf-day</p>
    </div>
    <p class="abs contact" style="top:429px">Lena Marchetti<br>Event Manager<br>Email: lena.marchetti@example.net</p>
  </section>

  <!-- Letter -->
  <section class="page page--letter">
    <div class="abs club" style="left:34px;top:17px">
      <div class="club-name" style="font-size:13px">Fairway<br>Eastbrook</div>
      <div class="club-mark" style="width:32px;height:32px"></div>
    </div>
    <p class="abs doc-title" style="top:77px">CHARITY GOLF DAY<br><em>SPONSORSHIP PROPOSAL</em></p>
    <div class="abs header-band" style="top:112px" role="img" aria-label="Decorative header band in blue, green and grey"></div>

    <p class="abs letter-lead">Join us for an exclusive day on the private Elmwood Golf Course, with all proceeds going to support Prostate Cancer Research, Awareness and Support.</p>

    <p class="abs letter-text" style="top:203px;width:300px">The Fairway Club of Eastbrook will again be holding its Charity Golf Day with all proceeds used to support the Prostate Cancer Research, awareness and Support Programs. The venue will be the prestigious Elmwood Golf Club on Friday 25 March 2022, with a shotgun start at 8:00 am.</p>
    <p class="abs letter-text" style="top:245px;width:300px">We have enclosed for your information a copy of our promotional sponsor packages that outline the event, sponsorship package options and inclusions.</p>
    <p class="abs letter-text" style="top:272px">The format of the day involves:</p>
    <ul class="abs letter-text ticks" style="top:289px">
      <li><svg viewBox="0 0 10 10"><circle cx="5" cy="5" r="4.2" fill="none" stroke="#1a1a1a" stroke-width="1"/><path d="M2.8,5 L4.6,6.8 L9,1.5" fill="none" stroke="#1a1a1a" stroke-width="1.2"/></svg>Player registration, refreshments and light breakfast from 7:00am</li>
      <li><svg viewBox="0 0 10 10"><circle cx="5" cy="5" r="4.2" fill="none" stroke="#1a1a1a" stroke-width="1"/><path d="M2.8,5 L4.6,6.8 L9,1.5" fill="none" stroke="#1a1a1a" stroke-width="1.2"/></svg>Ambrose competition starting at 8:00am</li>
      <li><svg viewBox="0 0 10 10"><circle cx="5" cy="5" r="4.2" fill="none" stroke="#1a1a1a" stroke-width="1"/><path d="M2.8,5 L4.6,6.8 L9,1.5" fill="none" stroke="#1a1a1a" stroke-width="1.2"/></svg>Two Course lunch and presentations in the club house from 12:30pm</li>
    </ul>
    <p class="abs letter-text letter-text--narrow" style="top:331px">Your commitment to supporting health programs in our community is truly appreciated. With assistance from sponsors such as yourself, we will continue to see improvements in the support and treatment for men and their families with prostate cancer.</p>
    <p class="abs letter-text letter-text--narrow" style="top:381px">We hope that you will consider supporting the worthwhile event that is open to any organisation or individual who wishes to enjoy the benefits of playing golf at the prestigious Elmwood Golf Club.</p>
    <p class="abs letter-text letter-text--narrow" style="top:422px">For more information, please check the website (www.fce.org.au/golf-day) or should you wish to discuss any aspect of the event, please contact me on 0400 555 123.</p>

    <p class="abs signoff" style="top:389px">Yours sincerely</p>
    <p class="abs signoff" style="top:417px">Maria (Kostas) Bellamy<br>Convener<br>Co - President 2021 -2022<br>Secretary 2021 - 2022<br>Fairway Club of Eastbrook</p>
  </section>

</main>
</body>
</html>
```